Motivational Quotes Poster Series

This is a 3 poster design series for Ridgeway Haul Academy. The size of each poster should be 18 inches wide and 24 inches tall. The goal of these posters is to serve as motivational "signs" to be hung in the office area for the employees (not customers). These employees are instructors/teachers, teaching students how to drive semi trucks. While each design is a separate poster and design, we're posting as 1 project because we'd like some continuity between the series. Below we'll break down the details of all 3 posters...

Poster #1
Text that must appear on poster - "If You Want The Best Out Of Each Student" and "Give The Best Of You!" Note: While this text must appear on the poster, you can arrange in the layout as you see fit. For example, first line could be at top of poster and second line on bottom.

Poster #2
Text that must appear on poster - "Invest In People" and "Change Someone's Life" (same notes apply as in 1st poster)

Poster #3
Text that must appear on poster - "Today Is..." and "Just Another Day For You" and "The Most Important Day In Their Life" Note: This can be laid out on the poster however you see fit, but each phrase needs to be separate and it needs to flow.

Target Market(s)

Truck Driver Training Instructors - These are middle-aged, mostly male, masculine type personalities.

Industry/Entity Type

Training

Requirements
Must have
• Must have noted text from description
Must have working files (ie - PSD, EPS, AI, etc) provided
Must have common theme between each poster in series
Must have easy to read font and layout
Must have product dimensions of 18 inches (width) by 24 inches (height). If design uses full dimensions please include quarter inch bleed.
Nice to have
• Nice to have a trucking theme...related to trucking industry, but not over the top. Example - This could mean subtle injection of background tire tracks, but by no means are tire tracks required.

For inspiration, you can visit the site at http://www.ridgewayhaulacademy.com. While you can use the colors of the site/logo, you can still branch out between each poster to try new colors within reason.

Note: While we've attached the logo to this project, it COULD be used but doesn't HAVE to be included in the design. The logo IS NOT a focal point. The phrases in the poster ARE the focal point.

```html
<!DOCTYPE html>
<html lang="en">
<head>
<meta charset="utf-8">
<title>Ridgeway Haul Academy – Motivational Poster Series</title>
<link rel="stylesheet" href="https://fonts.googleapis.com/css2?family=Questrial&display=swap">
<style>
  :root {
    --paper: #ffffff;
    --ink: #111111;
    --brick: #9e2424;
    --brick-ghost: #e6cdc3;
    --sky: #19a7e4;
    --sky-ghost: #cfeaf8;
    --lime: #8dbf3e;
    --lime-ghost: #e7f0d3;
    --mark: #555555;
  }
  html, body {
    margin: 0;
    padding: 0;
    width: 1200px;
    height: 534px;
    overflow: hidden;
    background: var(--paper);
  }
  .series {
    display: block;
    width: 1200px;
    height: 534px;
    font-family: "Questrial", "Century Gothic", sans-serif;
  }
  .headline { font-size: 58px; }
  .ghost-word { font-size: 118px; }
  .ink { fill: var(--ink); }
  .brick { fill: var(--brick); }
  .brick-ghost { fill: var(--brick-ghost); }
  .sky { fill: var(--sky); }
  .sky-ghost { fill: var(--sky-ghost); }
  .lime { fill: var(--lime); }
  .lime-ghost { fill: var(--lime-ghost); }
  .academy-mark { font-size: 7px; fill: var(--mark); }
</style>
</head>
<body>
<svg class="series" viewBox="0 0 1200 534" xmlns="http://www.w3.org/2000/svg">
  <defs>
    <linearGradient id="truck-brick" x1="0" y1="0" x2="1" y2="0">
      <stop offset="0" stop-color="#b04a44"/>
      <stop offset="1" stop-color="#f1e4e0"/>
    </linearGradient>
    <linearGradient id="truck-mono" x1="0" y1="0" x2="1" y2="1">
      <stop offset="0" stop-color="#e9e9e9"/>
      <stop offset="1" stop-color="#3a3a3a"/>
    </linearGradient>
    <linearGradient id="truck-silhouette" x1="0" y1="0" x2="1" y2="0">
      <stop offset="0" stop-color="#dcdcdc"/>
      <stop offset="1" stop-color="#1b1b1b"/>
    </linearGradient>
  </defs>

  <!-- Poster 1: Best of you -->
  <g class="poster poster-best">
    <g class="ghost-words">
      <text class="ghost-word brick-ghost" x="4" y="140" textLength="250" lengthAdjust="spacingAndGlyphs">BEST</text>
      <text class="ghost-word brick-ghost" x="4" y="250" textLength="250" lengthAdjust="spacingAndGlyphs">BEST</text>
      <text class="ghost-word brick-ghost" x="4" y="360" textLength="250" lengthAdjust="spacingAndGlyphs">BEST</text>
      <text class="ghost-word brick-ghost" x="4" y="470" textLength="250" lengthAdjust="spacingAndGlyphs">BEST</text>
    </g>
    <text class="headline brick" x="3" y="55" textLength="384" lengthAdjust="spacingAndGlyphs">IF YOU WANT</text>
    <text class="headline" x="3" y="110" textLength="374" lengthAdjust="spacingAndGlyphs"><tspan class="brick">THE </tspan><tspan class="ink">BEST</tspan></text>
    <text class="headline brick" x="3" y="160" textLength="384" lengthAdjust="spacingAndGlyphs">OUT OF EACH</text>
    <text class="headline brick" x="3" y="211" textLength="343" lengthAdjust="spacingAndGlyphs">STUDENT</text>
    <rect class="truck-art" x="0" y="282" width="300" height="84" fill="url(#truck-brick)" role="img" aria-label="Red-toned semi truck with trailer driving left to right"/>
    <text class="headline ink" x="3" y="442" textLength="384" lengthAdjust="spacingAndGlyphs">GIVE THE</text>
    <text class="headline" x="3" y="500" textLength="384" lengthAdjust="spacingAndGlyphs"><tspan class="brick">BEST </tspan><tspan class="ink">OF YOU!</tspan></text>
    <text class="academy-mark" x="160" y="522">Ridgeway Haul Academy</text>
  </g>

  <!-- Poster 2: Invest in people -->
  <g class="poster poster-people">
    <g class="ghost-words">
      <text class="ghost-word sky-ghost" x="408" y="150" textLength="370" lengthAdjust="spacingAndGlyphs">PEOPLE</text>
      <text class="ghost-word sky-ghost" x="408" y="240" textLength="370" lengthAdjust="spacingAndGlyphs">PEOPLE</text>
      <text class="ghost-word sky-ghost" x="408" y="330" textLength="370" lengthAdjust="spacingAndGlyphs">PEOPLE</text>
      <text class="ghost-word sky-ghost" x="408" y="420" textLength="370" lengthAdjust="spacingAndGlyphs">PEOPLE</text>
    </g>
    <text class="headline ink" x="408" y="68" font-size="70" textLength="372" lengthAdjust="spacingAndGlyphs">INVEST</text>
    <text class="headline sky" x="408" y="145" textLength="372" lengthAdjust="spacingAndGlyphs">IN PEOPLE</text>
    <rect class="truck-art" x="425" y="192" width="320" height="222" fill="url(#truck-mono)" role="img" aria-label="Black and white semi truck cab with trailer seen from the front corner"/>
    <text class="headline sky" x="408" y="456" font-size="64" textLength="336" lengthAdjust="spacingAndGlyphs">CHANGE</text>
    <text class="headline ink" x="408" y="502" font-size="42" textLength="356" lengthAdjust="spacingAndGlyphs">SOMEONE’S LIFE</text>
    <text class="academy-mark" x="555" y="522">Ridgeway Haul Academy</text>
  </g>

  <!-- Poster 3: Today is -->
  <g class="poster poster-today">
    <g class="ghost-words">
      <text class="ghost-word lime-ghost" x="870" y="130" textLength="320" lengthAdjust="spacingAndGlyphs">TODAY</text>
      <text class="ghost-word lime-ghost" x="870" y="220" textLength="320" lengthAdjust="spacingAndGlyphs">TODAY</text>
      <text class="ghost-word lime-ghost" x="870" y="310" textLength="320" lengthAdjust="spacingAndGlyphs">TODAY</text>
      <text class="ghost-word lime-ghost" x="870" y="400" textLength="320" lengthAdjust="spacingAndGlyphs">TODAY</text>
      <text class="ghost-word lime-ghost" x="870" y="490" textLength="320" lengthAdjust="spacingAndGlyphs">TODAY</text>
    </g>
    <text class="headline ink" x="803" y="56" textLength="365" lengthAdjust="spacingAndGlyphs">TODAY IS…</text>
    <text class="headline lime" x="803" y="158" font-size="40" textLength="370" lengthAdjust="spacingAndGlyphs">JUST ANOTHER DAY</text>
    <text class="headline lime" x="803" y="232" font-size="68" textLength="366" lengthAdjust="spacingAndGlyphs">FOR YOU</text>
    <rect class="truck-art" x="803" y="260" width="377" height="72" fill="url(#truck-silhouette)" role="img" aria-label="Silhouette of a semi truck with long trailer driving right to left"/>
    <text class="headline lime" x="803" y="410" font-size="66" textLength="370" lengthAdjust="spacingAndGlyphs">THE MOST</text>
    <text class="headline ink" x="803" y="462" textLength="370" lengthAdjust="spacingAndGlyphs">IMPORTANT</text>
    <text class="headline lime" x="803" y="502" font-size="40" textLength="370" lengthAdjust="spacingAndGlyphs">DAY IN THEIR LIFE</text>
    <text class="academy-mark" x="955" y="522">Ridgeway Haul Academy</text>
  </g>
</svg>
</body>
</html>
```